Preisliste für Kosmetikinstitut
Zielgruppe
Ich benötige für mein Kosmetikinstitut eine Preisliste für die moderne Frau, aber auch Männer. Das Design sollte mein Logo enthalten. Farben des Designkonzepts einbauen.
A4 quer zum Falten, wie ein Heft, 1. Seite Preisliste mit logo, im Innenteil dann Anwendungen
Aufgabenstellung
Minimalistisch, ästhetisch, modern, edel
Kontaktdaten auf der Rückseite
LT Hautatelier
Lena Tessmar
Lindenstieg 17
83671 Ostermoor
EMail: lena@lt-hautatelier.de
Whatsapp: 0176 284 9017

```html
<!DOCTYPE html>
<html lang="de">
<head>
<meta charset="utf-8">
<title>LT Hautatelier – Preisliste</title>
<link rel="stylesheet" href="https://fonts.googleapis.com/css2?family=Alegreya+Sans:wght@400;500;700&family=Cormorant+Garamond:wght@400;500&display=swap">
<style>
  :root {
    --backdrop: #d6d6d6;
    --cover: #dcdcdb;
    --cover-band: #e3e3e2;
    --paper: #ffffff;
    --paper-soft: #f4f4f4;
    --panel: #c9c9c7;
    --ink: #6f7472;
    --ink-strong: #5b605e;
    --ink-soft: #8b8f8d;
  }
  * { margin: 0; padding: 0; box-sizing: border-box; }
  html, body { width: 1200px; height: 800px; overflow: hidden; }
  body {
    background: var(--backdrop);
    font-family: "Alegreya Sans", sans-serif;
    color: var(--ink);
    position: relative;
  }
  .page {
    position: absolute;
    top: 142px;
    width: 364px;
    height: 515px;
    overflow: hidden;
  }

  /* Cover */
  .cover { left: 36px; background: var(--cover); }
  .cover__band {
    position: absolute; left: 64px; top: 0; width: 164px; height: 100%;
    background: var(--cover-band);
  }
  .cover__visual {
    position: absolute; left: 64px; top: 30px; width: 164px; height: 290px;
    background: linear-gradient(155deg, #e6e6e5 0%, #d9d9d8 45%, #e9e9e8 70%, #d6d6d5 100%);
  }
  .cover__brand {
    position: absolute; left: 64px; top: 168px; width: 164px;
    text-align: center;
    font-size: 13px; font-weight: 400; letter-spacing: 0.06em;
    color: var(--ink);
  }
  .cover__title {
    position: absolute; left: 0; right: 0; bottom: 58px;
    text-align: center; padding-left: 40px;
    font-family: "Cormorant Garamond", serif;
    font-size: 26px; font-weight: 400; letter-spacing: 0.32em;
    color: var(--ink-soft);
  }

  /* Inner spread */
  .inner-left { left: 440px; background: var(--paper); }
  .inner-right { left: 804px; background: var(--paper-soft); }
  .inner-left__visual {
    position: absolute; right: 0; top: 0; width: 88px; height: 206px;
    background: linear-gradient(170deg, #e4e4e4 0%, #c4c4c4 40%, #e8e8e8 70%, #bdbdbd 100%);
  }
  .inner-right__edge {
    position: absolute; left: 0; top: 0; width: 14px; height: 206px;
    background: linear-gradient(90deg, #b8b8b8, #cfcfcf);
  }
  .inner-right__panel {
    position: absolute; left: 20px; top: 20px; right: 20px; bottom: 20px;
    background: var(--panel);
    padding: 44px 26px 0 26px;
  }
  .inner-left__content { position: absolute; left: 34px; top: 40px; width: 226px; }

  .section-title {
    font-size: 10px; font-weight: 500; letter-spacing: 0.14em;
    text-transform: uppercase; color: var(--ink);
    margin-bottom: 18px;
  }
  .treatment { margin-bottom: 16px; }
  .treatment__row {
    display: flex; justify-content: space-between; align-items: baseline;
    font-size: 8.4px; font-weight: 700; letter-spacing: 0.1em;
    text-transform: uppercase; color: var(--ink-strong);
    line-height: 1.45;
  }
  .treatment__price {
    font-weight: 500; letter-spacing: 0.04em; white-space: nowrap;
    font-variant-numeric: oldstyle-nums;
  }
  .treatment__text {
    font-size: 7.4px; line-height: 1.55; color: var(--ink);
    margin-top: 6px;
  }
  .treatment__text + .treatment__text { margin-top: 5px; }
  .inner-right .treatment__text { color: #676b69; }
  .extras { margin-top: 22px; }
  .extras .section-title { font-weight: 700; font-size: 9.4px; margin-bottom: 10px; }
  .extras .treatment__row { font-size: 8.4px; }
  .extras .treatment__text { margin-top: 2px; }
</style>
</head>
<body>

  <section class="page cover" aria-label="Titelseite">
    <div class="cover__band"></div>
    <div class="cover__visual" role="img" aria-label="Hellgraue Cremetextur als Hintergrundbild"></div>
    <div class="cover__brand">LT Hautatelier</div>
    <h1 class="cover__title">PREISLISTE</h1>
  </section>

  <section class="page inner-left" aria-label="Innenseite links">
    <div class="inner-left__visual" role="img" aria-label="Nahaufnahme einer weißen Cremetextur"></div>
    <div class="inner-left__content">
      <h2 class="section-title">Apparative Behandlungen</h2>

      <div class="treatment">
        <div class="treatment__row"><span>Aquaclear – Treatment</span><span class="treatment__price">€ 59,00</span></div>
        <div class="treatment__row"><span>„Glowing Skin“</span></div>
        <p class="treatment__text">Für einen einmaligen Glow-Effekt: Die Haut wird tiefengereinigt, abgestorbene Verhornungen und Unreinheiten werden mit sanftem Peeling gelöst und die Poren in der Tiefe gereinigt.</p>
        <p class="treatment__text">Feuchtigkeitsspendende und pflegende Wirkstoffe werden eingeschleust, um die Haut zu nähren und den entstandenen Glow zu bewahren.</p>
        <p class="treatment__text">Hochkonzentrierte Wirkstoffessenzen werden auf die Haut aufgetragen, dank ihrer Molekularstruktur können sie tief eindringen.</p>
        <p class="treatment__text">Abschließend wird eine impulsgebende Maske aufgebracht; 60min</p>
      </div>

      <div class="treatment">
        <div class="treatment__row"><span>Mikrodermabrasion</span></div>
        <div class="treatment__row"><span>Gesicht</span><span class="treatment__price">€ 89,00</span></div>
        <div class="treatment__row"><span>Gesicht, Hals, Dekolleté</span><span class="treatment__price">€ 110,00</span></div>
        <p class="treatment__text">Die Mikrodermabrasion ist ein mechanisches Peeling, bei dem die Hornzellen sanft abgetragen und dann mit Hilfe eines Vakuums abgesaugt werden.</p>
        <p class="treatment__text">Die Behandlung fördert die Zellerneuerung und sorgt für ein glattes Gefühl. Pigmentflecken und Narben werden gemildert.</p>
        <p class="treatment__text">Die Haut wirkt ebenmäßig, entspannt und strahlt wieder.</p>
      </div>
    </div>
  </section>

  <section class="page inner-right" aria-label="Innenseite rechts">
    <div class="inner-right__edge"></div>
    <div class="inner-right__panel">
      <div class="treatment">
        <div class="treatment__row"><span>Microneedling</span></div>
        <div class="treatment__row"><span>Gesicht</span><span class="treatment__price">€ 110,00</span></div>
        <div class="treatment__row"><span>Gesicht, Hals</span><span class="treatment__price">€ 130,00</span></div>
        <div class="treatment__row"><span>Gesicht, Hals, Dekolleté</span><span class="treatment__price">€ 150,00</span></div>
        <p class="treatment__text">Die Behandlung eignet sich besonders für Menschen, die ihre Hautqualität verbessern und Falten, (Akne)Narben, Pigmentverschiebungen, große Poren und sogar Haarausfall behandeln wollen.</p>
        <p class="treatment__text">Mit Hilfe feinster Nadeln werden der Haut kontrolliert Mikroverletzungen zugeführt, dies regt die natürliche Wundheilung, sowie Kollagen- und Elastin Bildung an.</p>
        <p class="treatment__text">Microneedling ist also eine natürliche Beauty-Behandlung, die körpereigene Reparaturmechanismen nutzt, um ein strafferes Hautbild zu erhalten. Bereits nach der ersten Behandlung sieht die Haut aufgepolstert, frisch und rosig aus.</p>
        <p class="treatment__text">Kleine Linien und Fältchen werden tiefenbehandelt. Die Haut wirkt straffer und jugendlicher. Ein weiterer Vorteil, durch die Stichkanäle können Wirkstoffe besser von der Haut aufgenommen werden.</p>
      </div>

      <div class="extras">
        <h2 class="section-title">Zusatzleistungen</h2>
        <div class="treatment__row"><span>Augenbrauen zupfen</span><span class="treatment__price">€ 08,00</span></div>
        <div class="treatment__row"><span>Augenbrauen färben</span><span class="treatment__price">€ 12,00</span></div>
        <div class="treatment__row"><span>Wimpern färben</span><span class="treatment__price">€ 15,00</span></div>
        <div class="treatment__row"><span>Enthaarung</span><span class="treatment__price">€ 10,00-30,00</span></div>
        <p class="treatment__text">Enthaarung der störenden<br>Gesichtsbehaarung mittels Wax.</p>
      </div>
    </div>
  </section>

</body>
</html>
```